Yacht Charter Broker needs a magazine page design

We are a travel agent for yachts called Velmora Yacht Charters. www.velmoracharters.example We are advertising in a magazine at the grand invitational trotter pony fair - https://gipfairground.example/ - and need a high-end luxury feeling magazine page.

Target Market(s)

Vacation goers looking to charter a crewed yacht.

Industry/Entity Type

Travel Agent

Requirements
Must have
• luxury feel. logo. website and social media icons if you feel necessary. Our motto is: Inhale. Exhale. Sail.
• Catamaran picture, snorkeling and other island, water looking pictures.
Nice to have
• Open to your design.
Should not have
• Nothing comes to mind.

```html
<!DOCTYPE html>
<html lang="en">
<head>
<meta charset="utf-8">
<title>Velmora Yacht Charters – Magazine Page</title>
<link rel="stylesheet" href="https://fonts.googleapis.com/css2?family=Montserrat:wght@700;800&family=Raleway:wght@400;500;600&family=Cinzel:wght@500&display=swap">
<style>
  :root {
    --navy: #14235c;
    --ink: #1f2433;
    --grey: #6f7074;
    --rule: #c9cbd1;
    --paper: #ffffff;
    --backdrop: #e9e7e3;
    --sky: #9fb7cf;
    --sea: #1d7fa6;
    --lagoon: #3fc0c8;
    --deck: #8a5a3a;
  }
  * { margin: 0; padding: 0; box-sizing: border-box; }
  html, body { width: 1200px; height: 2365px; overflow: hidden; }
  body { background: var(--backdrop); position: relative; font-family: "Raleway", sans-serif; color: var(--ink); }

  .page {
    position: absolute; left: 50px; top: 406px;
    width: 1100px; height: 1552px;
    background: var(--paper);
    box-shadow: 0 6px 18px rgba(0,0,0,.18);
  }

  .brand { position: absolute; top: 88px; left: 0; width: 100%; text-align: center; }
  .brand-name {
    font-family: "Raleway", sans-serif; font-weight: 500;
    font-size: 66px; letter-spacing: 10px; color: var(--navy); line-height: 1;
  }
  .brand-tagline {
    margin-top: 8px; font-family: "Cinzel", serif; font-weight: 500;
    font-size: 17px; letter-spacing: 3px; color: var(--navy);
    padding-left: 240px;
  }

  .hero {
    position: absolute; left: 78px; top: 232px; width: 944px; height: 708px;
    background: linear-gradient(180deg, var(--sky) 0%, #d8dee4 45%, #6b92ad 72%, var(--deck) 86%, #6e4429 100%);
  }

  .gallery {
    position: absolute; left: 78px; top: 957px; width: 944px; height: 166px;
    display: grid; grid-template-columns: repeat(4, 1fr); gap: 12px;
  }
  .gallery-item { height: 100%; }
  .gallery-item.swim { background: linear-gradient(180deg, #7fb3dc 0%, #b8d9ea 40%, var(--lagoon) 70%, #1a9bb0 100%); }
  .gallery-item.lookout { background: linear-gradient(180deg, #b9d6ee 0%, #e7eef3 60%, #ffffff 100%); }
  .gallery-item.snorkel { background: linear-gradient(180deg, #6f8c7a 0%, #6d7d70 35%, #3fc6c0 65%, #18a3a8 100%); }
  .gallery-item.aerial { background: linear-gradient(135deg, #0f6f9b 0%, var(--sea) 55%, #0b5f88 100%); }

  .headline {
    position: absolute; left: 0; top: 1180px; width: 100%; text-align: center;
    font-family: "Montserrat", sans-serif; font-weight: 800;
    font-size: 38px; color: var(--navy); letter-spacing: .5px;
  }
  .intro {
    position: absolute; left: 90px; top: 1242px; width: 920px;
    font-size: 19.5px; line-height: 1.2; text-align: justify; text-align-last: left;
    color: var(--ink);
  }

  .contact-bar {
    position: absolute; left: 90px; top: 1432px; width: 920px; height: 70px;
    display: flex; align-items: center;
  }
  .social { display: flex; gap: 12px; padding-right: 26px; }
  .social-dot {
    width: 42px; height: 42px; border-radius: 50%;
    border: 2px solid var(--rule); background: var(--paper);
  }
  .divider { width: 2px; height: 64px; background: var(--rule); }
  .website {
    flex: 1; padding-left: 36px;
    font-family: "Raleway", sans-serif; font-weight: 600; font-size: 25px; color: var(--ink);
  }
  .phones { padding-left: 28px; font-size: 22px; line-height: 1.45; color: var(--ink); }

  .footer-band { position: absolute; left: 0; bottom: 0; width: 100%; height: 24px; display: flex; }
  .footer-band .navy { width: 55%; background: var(--navy); }
  .footer-band .grey { width: 45%; background: var(--grey); }
</style>
</head>
<body>
  <main class="page">
    <header class="brand">
      <div class="brand-name">VELMORA</div>
      <div class="brand-tagline">YACHT CHARTER BROKER</div>
    </header>

    <div class="hero" role="img" aria-label="Woman at the rail of a sailing yacht's teak deck under full white sails, looking out over the open sea"></div>

    <div class="gallery">
      <div class="gallery-item swim" role="img" aria-label="Swimmer with raised arms in clear turquoise water"></div>
      <div class="gallery-item lookout" role="img" aria-label="Child in a captain's cap looking out from a yacht"></div>
      <div class="gallery-item snorkel" role="img" aria-label="Snorkeler among granite boulders in a clear lagoon"></div>
      <div class="gallery-item aerial" role="img" aria-label="Aerial view of a white yacht on deep blue water"></div>
    </div>

    <h1 class="headline">WE ARE THE LEADERS IN YACHT CHARTERING</h1>

    <p class="intro">Velmora was created to disrupt the yacht charter broker community. To bring a white glove level of service to an industry where the clientele demands it. The lost art of communication and transparency has been reintroduced. A strict adherence to ethical and fiduciary responsibilities exists again. Built from frustration by forward-thinking professionals with a level of passion and commitment rarely seen in business anymore. Beyond yachts, we think bigger. Unbiased advice. Detailed obsession. Innovative. Motivated. Accountable. Client-centric.</p>

    <div class="contact-bar">
      <div class="social">
        <span class="social-dot"></span>
        <span class="social-dot"></span>
        <span class="social-dot"></span>
        <span class="social-dot"></span>
      </div>
      <span class="divider"></span>
      <div class="website">www.velmoracharters.example</div>
      <span class="divider"></span>
      <div class="phones">
        <div>Miles: 555.014.0295</div>
        <div>Clara: 555.014.0296</div>
      </div>
    </div>

    <div class="footer-band"><span class="navy"></span><span class="grey"></span></div>
  </main>
</body>
</html>
```